Consumer Facing Energy Data Analytics Startup Needs a Postcard to Promote New Product

We need a set of 2 postcards (6 x 4.25 inches as describers in the attached files) to help us promote our product for a new company based in San Francisco called "Lumo Crest".
We develop an alert platform for customers of energy utility companies. Our initial product is "Lumo Signal" - an application that helps people better manage their energy bill by sending an SMS or email alter in advance of a high bill.
We would like to see designs that use the colors blue and orange (same as in the website: www.lumocrest.example). The text of the postcards will be reworked once a layout has been chosen, but we welcome original ways to attract the customers' attention.
Our goal is ultimately to have our targets go the our website and sign up for our service.
The final deliverable should be 8 vector files (preferable .eps, 4 file types, one version in print and one in web format):
- front of card for our small and medium business customers
- front of card for our residential customers
- back of card for our small and medium business customers
- back of card for our residential customers
- DINPro and Avenir

```html
<!DOCTYPE html>
<html lang="en">
<head>
<meta charset="utf-8">
<title>Lumo Crest – Lumo Signal Postcards</title>
<link rel="stylesheet" href="https://fonts.googleapis.com/css2?family=Nunito+Sans:wght@400;600;700;800&family=Open+Sans:wght@400;600;700;800&display=swap">
<style>
  :root {
    --stage: #0c5474;
    --brand-blue: #2ea6de;
    --brand-orange: #f5a623;
    --pill-orange: #f8ab3c;
    --ink: #1f2a33;
    --ink-soft: #5d6770;
    --tag-grey: #7a8690;
    --card-white: #ffffff;
    --wash-blue: #d6e9f6;
    --wash-pale: #f2f8fd;
    --photo-tone: #c3d0db;
    --photo-tone-deep: #a9b6c1;
    --mail-blue: #42addb;
    --mail-blue-dark: #2f97c6;
  }
  * { box-sizing: border-box; margin: 0; padding: 0; }
  html, body { width: 1200px; height: 1000px; overflow: hidden; }
  body {
    background: var(--stage);
    font-family: "Nunito Sans", "Avenir", sans-serif;
    position: relative;
  }

  /* ---------- Back of card ---------- */
  .card-back {
    position: absolute; left: 40px; top: 32px; width: 690px; height: 535px;
    background:
      linear-gradient(115deg, rgba(255,255,255,0) 40%, rgba(255,255,255,.7) 41%, rgba(255,255,255,0) 60%),
      linear-gradient(160deg, var(--wash-blue) 0%, var(--wash-pale) 45%, var(--card-white) 80%);
    overflow: hidden;
  }
  .postage-window {
    position: absolute; left: 532px; top: 36px; width: 128px; height: 124px;
    background: rgba(150,160,170,.35);
  }
  .brand-lockup { position: absolute; display: flex; align-items: center; }
  .brand-lockup .brand-dot { border-radius: 50%; background: var(--brand-orange); flex: none; }
  .brand-lockup .brand-name { color: var(--brand-blue); font-weight: 600; letter-spacing: .08em; line-height: 1; white-space: nowrap; }
  .brand-tagline { position: absolute; color: var(--tag-grey); letter-spacing: .06em; white-space: nowrap; }

  .card-back .brand-lockup { left: 98px; top: 34px; gap: 8px; }
  .card-back .brand-dot { width: 30px; height: 30px; }
  .card-back .brand-name { font-size: 20px; }
  .card-back .brand-tagline { left: 138px; top: 59px; font-size: 7px; }

  .email-preview {
    position: absolute; left: 71px; top: 78px; width: 203px; height: 188px;
    background: var(--card-white);
    font-family: "Open Sans", sans-serif;
  }
  .email-header {
    height: 75px; background: var(--mail-blue); text-align: center; color: #fff;
    border-top: 10px solid var(--card-white); position: relative;
  }
  .email-header .label-band { height: 18px; background: var(--mail-blue-dark); position: relative; }
  .email-header .badge {
    position: absolute; left: 94px; top: -8px; width: 14px; height: 14px; border-radius: 50%;
    background: var(--brand-orange);
  }
  .email-header .label { font-size: 5px; letter-spacing: .1em; padding-top: 8px; }
  .email-header .risk { font-size: 4px; margin-top: 6px; opacity: .9; }
  .email-header .increase { font-size: 8px; font-family: Georgia, serif; }
  .email-header .increase b { color: #ffc843; }
  .email-header .cycle {
    margin: 3px auto 0; width: 96px; height: 11px; background: #fff; border-radius: 2px;
    font-size: 4px; color: var(--ink-soft); line-height: 11px;
  }
  .email-header .cycle b { color: var(--brand-orange); font-size: 5px; }
  .email-intro { font-size: 5px; color: var(--ink-soft); text-align: center; margin-top: 11px; }
  .tip-row { display: flex; justify-content: space-between; padding: 6px 6px 0; }
  .tip { width: 58px; text-align: center; }
  .tip .tip-icon { width: 30px; height: 20px; margin: 0 auto; background: #d9dee2; border-radius: 3px; }
  .tip h4 { font-size: 3.6px; font-weight: 700; color: var(--ink); margin-top: 5px; }
  .tip p { font-size: 3.2px; color: var(--ink-soft); margin-top: 3px; line-height: 1.4; height: 26px; }
  .tip .tip-button {
    display: block; width: 30px; height: 8px; margin: 4px auto 0; background: var(--brand-orange);
    color: #fff; font-size: 3px; line-height: 8px;
  }

  .back-copy {
    position: absolute; left: 30px; top: 280px; width: 288px; text-align: center;
    font-size: 15.5px; line-height: 20.5px; color: var(--ink);
  }
  .back-url {
    position: absolute; left: 20px; top: 405px; width: 308px; text-align: center;
    font-size: 23px; font-weight: 800; color: var(--brand-orange);
  }

  /* ---------- Front of card ---------- */
  .card-front {
    position: absolute; left: 436px; top: 418px; width: 707px; height: 547px;
    background:
      linear-gradient(125deg, rgba(255,255,255,0) 30%, rgba(255,255,255,.55) 31%, rgba(255,255,255,0) 55%),
      linear-gradient(180deg, var(--wash-blue) 0%, var(--wash-pale) 60%, var(--card-white) 100%);
    overflow: hidden;
    box-shadow: -6px 8px 22px rgba(0,0,0,.35);
  }
  .family-photo {
    position: absolute; left: 340px; top: 0; width: 367px; height: 547px;
    background: linear-gradient(90deg, rgba(195,208,219,0) 0%, var(--photo-tone) 35%, var(--photo-tone-deep) 100%);
  }
  .card-front .brand-lockup { left: 164px; top: 36px; gap: 40px; }
  .card-front .brand-dot { width: 62px; height: 62px; }
  .card-front .brand-name { font-size: 36px; }
  .card-front .brand-tagline { left: 272px; top: 80px; font-size: 14px; letter-spacing: .02em; }

  .feature-list { position: absolute; left: 32px; top: 117px; list-style: none; }
  .feature { display: flex; align-items: center; height: 86px; position: relative; }
  .feature-mascot {
    width: 80px; height: 80px; border-radius: 50%; flex: none;
    background: radial-gradient(circle at 40% 35%, #e8f5fd 0%, #7cc4ea 60%, #2f8fc6 100%);
    border: 2px solid #b9dff3;
  }
  .feature-pill {
    margin-left: 5px; width: 305px; height: 76px; border-radius: 38px;
    background: var(--pill-orange); text-align: center; font-family: "Open Sans", sans-serif;
    color: var(--ink); padding-top: 6px;
  }
  .feature-pill h3 { font-size: 27px; line-height: 32px; color: #fff; font-weight: 400; letter-spacing: .01em; }
  .feature-pill h3 b { font-weight: 800; }
  .feature-pill p { font-size: 9.5px; font-weight: 700; line-height: 13px; text-transform: uppercase; }

  .front-strap {
    position: absolute; left: 0; top: 470px; width: 560px; text-align: center;
    font-family: "Open Sans", sans-serif; font-size: 13px; color: var(--ink); text-transform: uppercase;
  }
  .front-cta {
    position: absolute; left: 0; top: 492px; width: 560px; text-align: center;
    font-family: "Open Sans", sans-serif; font-size: 24px; color: var(--ink); text-transform: uppercase;
  }
</style>
</head>
<body>

<section class="card-back" aria-label="Postcard back">
  <div class="postage-window"></div>

  <div class="brand-lockup">
    <span class="brand-dot"></span>
    <span class="brand-name">LUMO CREST</span>
  </div>
  <div class="brand-tagline">ENERGY ANALYTICS AND INSIGHTS</div>

  <div class="email-preview">
    <div class="email-header">
      <span class="badge"></span>
      <div class="label">- LUMO SIGNAL -</div>
      <div class="risk">You're at risk of a higher than average energy bill</div>
      <div class="increase">Bill increase from last month: <b>30%</b></div>
      <div class="cycle"><b>10 days</b> left in your billing cycle</div>
    </div>
    <div class="email-intro">Things you can do right now to lower your risk of high energy bills.</div>
    <div class="tip-row">
      <div class="tip">
        <div class="tip-icon"></div>
        <h4>Inform the Household</h4>
        <p>Let everyone at home know the goal to save energy this month.</p>
        <span class="tip-button">I DID IT</span>
      </div>
      <div class="tip">
        <div class="tip-icon"></div>
        <h4>Enable Power Save Modes</h4>
        <p>Many devices have power save modes you can turn on when idle.</p>
        <span class="tip-button">I DID IT</span>
      </div>
      <div class="tip">
        <div class="tip-icon"></div>
        <h4>Cold cycle your laundry</h4>
        <p>Running your washer on a cold cycle uses far less energy overall.</p>
        <span class="tip-button">I DID IT</span>
      </div>
    </div>
  </div>

  <p class="back-copy">Lumo Crest employs advanced analytics software to assess customer energy use on a daily basis. We predict monthly energy bills based on current usage, and provide customer alerts and tips when use is above normal.</p>
  <p class="back-url">www.lumocrest.example</p>
</section>

<section class="card-front" aria-label="Postcard front">
  <div class="family-photo" role="img" aria-label="Photo of a smiling family of four standing on the lawn in front of their house"></div>

  <div class="brand-lockup">
    <span class="brand-dot"></span>
    <span class="brand-name">LUMO CREST</span>
  </div>
  <div class="brand-tagline">ENERGY ANALYTICS AND INSIGHTS</div>

  <ul class="feature-list">
    <li class="feature">
      <div class="feature-mascot" role="img" aria-label="Cartoon light bulb character with glasses holding a pointer"></div>
      <div class="feature-pill">
        <h3><b>LUMO</b> SIGNAL</h3>
        <p>Never get the bad surprise<br>of a high energy bill again with Lumo Signal.</p>
      </div>
    </li>
    <li class="feature">
      <div class="feature-mascot" role="img" aria-label="Cartoon light bulb character holding a phone"></div>
      <div class="feature-pill">
        <h3><b>LUMO</b> SIGNAL</h3>
        <p>Our email alerts will put you in control<br>of your energy usage.</p>
      </div>
    </li>
    <li class="feature">
      <div class="feature-mascot" role="img" aria-label="Cartoon light bulb character holding a bill"></div>
      <div class="feature-pill">
        <h3><b>LUMO</b> SIGNAL</h3>
        <p>Get your alerts on the go by<br>email or SMS so you're always in control.</p>
      </div>
    </li>
    <li class="feature">
      <div class="feature-mascot" role="img" aria-label="Cartoon light bulb character holding a banknote"></div>
      <div class="feature-pill">
        <h3><b>LUMO</b> SIGNAL</h3>
        <p>Save on your energy expenses with our<br>simple and easy timely recommendations.</p>
      </div>
    </li>
  </ul>

  <p class="front-strap">Lumo Crest helps you predict and avoid your high energy bills.</p>
  <p class="front-cta">Visit now : www.lumocrest.example</p>
</section>

</body>
</html>
```